Full Business Set-Up Stationary, Folder, Envelope, & Business Card, etc. CPA Firm
CPA Firm Collarteral Package
Full Business Set-Up Stationary, Folder, Envelope, & Business Card, etc. CPA Firm - Consulting
Creative Brief
Bright & Fun-filled
Marla Penn, CPA
Certified Public Accountant
512 Hadley Court Suite 200 Oakmere, FL 40217
MarlaPenn@ledgerbox.example
www.MarlaPennCPA.example
RT58163
Key Words: CPA since 1999 Servicing State of Florida since 1999 Certified Management Accountant Certified Public Accounting Firm Award Winning CPA Award Winning Professional Officies Located in the Oakmere Civic Trade Hall Trustworthy, Professional, Experienced
Tag Line: See the Clarity TrueMark Services
marlapenn marlapenn
Thanks for your submissions. Please include portfolio for the Firm. Particularly a Business Folder and Letterhead/Envelope. Ipad and Iphone Designs.

```html
<!DOCTYPE html>
<html lang="en">
<head>
<meta charset="utf-8">
<title>Marla Penn, CPA — Business Card</title>
<link href="https://fonts.googleapis.com/css2?family=Cinzel:wght@400;600&family=EB+Garamond:wght@400;500&display=swap" rel="stylesheet">
<style>
  :root {
    --bg: #6f7276;
    --blue-deep: #1b6fc2;
    --blue: #2a8be0;
    --blue-light: #4aa8ee;
    --green: #8cc63f;
    --white: #ffffff;
    --ink-blue: #1f74c6;
  }
  * { box-sizing: border-box; margin: 0; padding: 0; }
  html, body { width: 1200px; height: 908px; overflow: hidden; }
  body {
    background: var(--bg);
    display: flex;
    align-items: center;
    justify-content: center;
    gap: 40px;
  }
  .card {
    position: relative;
    width: 540px;
    height: 309px;
    border-radius: 16px;
    overflow: hidden;
    box-shadow: 0 10px 24px rgba(0,0,0,0.3);
  }
  /* Front */
  .card-front {
    background: linear-gradient(135deg, var(--blue-light) 0%, var(--blue) 50%, var(--blue-deep) 100%);
    color: var(--white);
  }
  .front-mark {
    position: absolute;
    right: 40px;
    top: 40px;
    width: 200px;
    height: 200px;
    border-radius: 50%;
    background: rgba(255,255,255,0.12);
  }
  .front-name {
    position: absolute;
    left: 34px;
    top: 118px;
    font-family: "Cinzel", serif;
    font-size: 30px;
    font-weight: 400;
    letter-spacing: 0.5px;
    line-height: 1;
  }
  .front-tagline {
    position: absolute;
    left: 36px;
    top: 154px;
    font-family: "Cinzel", serif;
    font-size: 11.5px;
    letter-spacing: 5.2px;
  }
  /* Back */
  .card-back { background: var(--blue); }
  .card-back svg.shape { position: absolute; inset: 0; }
  .brand {
    position: absolute;
    left: 40px;
    top: 52px;
    display: flex;
    align-items: center;
    gap: 12px;
    font-family: "Cinzel", serif;
    color: var(--ink-blue);
    font-size: 24px;
  }
  .brand-dot {
    width: 34px; height: 34px;
    border-radius: 50%;
    background: var(--green);
  }
  .back-tagline {
    position: absolute;
    left: 86px;
    top: 88px;
    font-family: "Cinzel", serif;
    font-size: 9px;
    letter-spacing: 4px;
    color: var(--ink-blue);
  }
  .back-name {
    position: absolute;
    left: 40px;
    bottom: 56px;
    font-family: "Cinzel", serif;
    font-size: 22px;
    color: var(--white);
  }
  .back-title {
    position: absolute;
    left: 40px;
    bottom: 34px;
    font-family: "EB Garamond", serif;
    font-variant: small-caps;
    font-size: 17px;
    letter-spacing: 1px;
    color: var(--white);
  }
  .contact {
    position: absolute;
    right: 26px;
    top: 34px;
    width: 190px;
    list-style: none;
    font-family: "EB Garamond", serif;
    font-size: 13px;
    line-height: 1.45;
    color: var(--white);
  }
  .contact li { display: flex; align-items: center; gap: 6px; }
  .contact .license { margin-bottom: 6px; }
  .contact svg { width: 11px; height: 11px; flex: none; }
</style>
</head>
<body>
  <section class="card card-front">
    <div class="front-mark"></div>
    <h1 class="front-name">Marla Penn CPA</h1>
    <p class="front-tagline">See the Clarity</p>
  </section>

  <section class="card card-back">
    <svg class="shape" viewBox="0 0 540 309" preserveAspectRatio="none">
      <path d="M0 0 H330 C310 120 240 200 0 232 Z" fill="var(--green)"/>
      <path d="M0 0 H318 C298 112 228 188 0 220 Z" fill="var(--white)"/>
    </svg>
    <div class="brand"><span class="brand-dot"></span>Marla Penn CPA</div>
    <p class="back-tagline">See the Clarity</p>
    <ul class="contact">
      <li class="license">License No. RT58163</li>
      <li>512 Hadley Court Suite 200</li>
      <li>Oakmere, FL 40217</li>
      <li><svg viewBox="0 0 12 12"><circle cx="6" cy="6" r="5.5" fill="none" stroke="#fff"/><path d="M4 3.5 L5 5 L4.5 6 Q5.5 7.5 6.5 8 L7.5 7.4 L9 8.4" fill="none" stroke="#fff" stroke-width="0.9"/></svg>(555) 014-2286</li>
      <li><svg viewBox="0 0 12 12"><circle cx="6" cy="6" r="5.5" fill="none" stroke="#fff"/><rect x="3.5" y="4" width="5" height="4" fill="none" stroke="#fff" stroke-width="0.9"/></svg>(555) 014-2291</li>
      <li><svg viewBox="0 0 12 12"><circle cx="6" cy="6" r="5.5" fill="none" stroke="#fff"/><path d="M3 4 H9 V8 H3 Z M3 4 L6 6.3 L9 4" fill="none" stroke="#fff" stroke-width="0.9"/></svg>MarlaPenn@ledgerbox.example</li>
      <li><svg viewBox="0 0 12 12"><circle cx="6" cy="6" r="5.5" fill="none" stroke="#fff"/><path d="M1 6 H11 M6 1 Q3 6 6 11 Q9 6 6 1" fill="none" stroke="#fff" stroke-width="0.9"/></svg>www.MarlaPennCPA.example</li>
    </ul>
    <h2 class="back-name">Marla Penn, CPA</h2>
    <p class="back-title">Certified Public Accountant</p>
  </section>
</body>
</html>
```